Recruitment talent email to send employers

We are a recruitment company specialising in STEM talent. We're after an eye catching email design to send our clients (ie employers) information about our top cadidates.

Target Market(s)

Employers

Requirements
Must have
• Must be clean/fresh looking, professional and concise

```html
<!DOCTYPE html>
<html lang="en">
<head>
<meta charset="utf-8">
<title>Vector Talent – Employer Email</title>
<link rel="stylesheet" href="https://fonts.googleapis.com/css2?family=Montserrat:wght@400;600;700&family=Open+Sans:ital,wght@0,400;0,600;0,700;1,400&display=swap">
<style>
  :root {
    --page: #ffffff;
    --blue: #1e6ac8;
    --blue-deep: #1658b4;
    --blue-soft: #2f7ad6;
    --card: #4f97e5;
    --card-edge: #5ea2ea;
    --pill: #1552a8;
    --green: #25a829;
    --green-dark: #1b8f20;
    --white: #ffffff;
    --line: rgba(255,255,255,0.55);
    --bubble: rgba(120,175,240,0.45);
    --avatar: #b9b4ae;
  }
  * { box-sizing: border-box; margin: 0; padding: 0; }
  html, body { width: 1200px; height: 2217px; overflow: hidden; background: var(--page); }
  body { position: relative; font-family: "Open Sans", Arial, sans-serif; color: var(--white); }

  .email {
    position: absolute; top: 44px; width: 556px; height: 2134px; overflow: hidden;
    background: linear-gradient(180deg, var(--blue) 0%, var(--blue-deep) 55%, var(--blue-soft) 88%, #3a84db 100%);
  }
  .email--tinted { left: 30px; }
  .email--photo { left: 614px; }

  .hero { position: absolute; left: 0; top: 0; width: 556px; height: 367px; }
  .hero__image { position: absolute; inset: 0; }
  .email--tinted .hero__image { background: linear-gradient(180deg, #5b8fcf 0%, #4f8ad2 55%, #5a98e2 100%); }
  .email--photo .hero__image { background: linear-gradient(180deg, #6b6a63 0%, #4d4c47 55%, #35332f 100%); }
  .hero__title {
    position: absolute; left: 0; width: 100%; text-align: center;
    font-family: "Montserrat", Arial, sans-serif; font-weight: 700; letter-spacing: 0.5px;
  }
  .email--tinted .hero__title { top: 146px; font-size: 40px; line-height: 50px; }
  .email--photo .hero__title { top: 214px; font-size: 49px; line-height: 60px; }
  .hero__subtitle {
    position: absolute; top: 196px; left: 0; width: 100%; text-align: center;
    font-size: 17px; font-weight: 400;
  }
  .hero__actions { position: absolute; left: 151px; height: 30px; display: flex; align-items: center; }
  .email--tinted .hero__actions { top: 291px; }
  .email--photo .hero__actions { top: 326px; }

  .button {
    display: inline-flex; align-items: center; justify-content: center; gap: 8px;
    height: 30px; border-radius: 3px; background: linear-gradient(180deg, var(--green), var(--green-dark));
    box-shadow: 0 3px 6px rgba(0,0,0,0.25);
    font-size: 11px; font-weight: 600; color: var(--white);
  }
  .button--start { width: 100px; }
  .hero__or { margin: 0 14px 0 16px; font-size: 12px; }
  .hero__link { font-size: 11px; font-weight: 600; text-decoration: underline; }

  .section-title {
    position: absolute; left: 0; width: 100%; text-align: center;
    font-family: "Montserrat", Arial, sans-serif; font-weight: 400; font-size: 30px; line-height: 38px;
  }
  .ceo__title { top: 448px; }
  .ceo__intro {
    position: absolute; top: 496px; left: 0; width: 100%; text-align: center;
    font-size: 12.5px; line-height: 18px;
  }
  .ceo__art { position: absolute; left: 0; top: 560px; width: 556px; height: 260px; }

  .candidates__backdrop {
    position: absolute; left: 0; top: 930px; width: 556px; height: 880px;
    background: linear-gradient(180deg, rgba(10,50,120,0) 0%, rgba(10,50,120,0.28) 25%, rgba(10,50,120,0.22) 70%, rgba(10,50,120,0) 100%);
  }
  .candidates__title { top: 868px; }
  .grid-line { position: absolute; background: var(--line); }
  .grid-line--v { left: 277px; top: 1012px; width: 1px; height: 655px; }
  .grid-line--h1 { left: 95px; top: 1182px; width: 366px; height: 1px; }
  .grid-line--h2 { left: 95px; top: 1447px; width: 366px; height: 1px; }

  .candidate {
    position: absolute; width: 202px; height: 170px; border-radius: 5px;
    background: linear-gradient(180deg, var(--card-edge), var(--card));
    box-shadow: 0 4px 10px rgba(0,30,80,0.25); text-align: center;
  }
  .candidate--left { left: 46px; }
  .candidate--right { left: 307px; }
  .candidate--r1 { top: 1030px; }
  .candidate--r2 { top: 1291px; }
  .candidate--r3 { top: 1557px; }
  .candidate__avatar {
    position: absolute; left: 64px; top: -41px; width: 74px; height: 74px; border-radius: 50%;
    background: radial-gradient(circle at 50% 40%, #d6d1cb, var(--avatar));
    border: 2px solid var(--white);
  }
  .candidate__name { position: absolute; top: 46px; width: 100%; font-size: 16px; font-weight: 700; }
  .candidate__role { position: absolute; top: 68px; width: 100%; font-size: 10px; font-style: italic; }
  .candidate__bio { position: absolute; top: 90px; left: 14px; right: 14px; font-size: 12.5px; line-height: 18px; }
  .candidate__more { position: absolute; top: 146px; left: 91px; }

  .view-all { position: absolute; left: 229px; top: 1729px; width: 100px; }

  .footer__brand {
    position: absolute; top: 1844px; left: 0; width: 100%; text-align: center;
    font-family: "Montserrat", Arial, sans-serif; font-weight: 700; font-size: 26px; line-height: 34px;
  }
  .footer__nav {
    position: absolute; top: 1884px; left: 0; width: 100%; display: flex; justify-content: center; gap: 24px;
    font-size: 11.5px; letter-spacing: 1px; text-transform: uppercase;
  }
  .footer__text {
    position: absolute; top: 1925px; left: 0; width: 100%; text-align: center; font-size: 12px; line-height: 18px;
  }
  .contact {
    position: absolute; left: 164px; top: 1970px; width: 228px; height: 37px; border-radius: 19px;
    background: var(--pill); display: flex; align-items: center;
    font-size: 13px; font-weight: 600;
  }
  .contact__icon { width: 31px; height: 31px; margin: 0 22px 0 3px; border-radius: 50%; background: var(--white); display: flex; align-items: center; justify-content: center; }
  .social { position: absolute; top: 2050px; left: 0; width: 100%; display: flex; justify-content: center; gap: 16px; }
  .social__dot { width: 11px; height: 11px; border-radius: 50%; background: var(--white); }
  .footer__copy { position: absolute; top: 2076px; left: 0; width: 100%; text-align: center; font-size: 10.5px; }
</style>
</head>
<body>

<!-- Variant A: tinted hero -->
<section class="email email--tinted">
  <header class="hero">
    <div class="hero__image" role="img" aria-label="Candidates seated in a row with laptops and a sketched robot, tinted blue"></div>
    <h1 class="hero__title">VECTOR TALENT</h1>
    <p class="hero__subtitle">Lorem ipsum dolor sit amet, consectetur adipiscing</p>
    <div class="hero__actions">
      <span class="button button--start">Get Started
        <svg width="11" height="11" viewBox="0 0 12 12"><circle cx="6" cy="6" r="6" fill="#fff"/><path d="M5 3.5 7.5 6 5 8.5" stroke="#1b8f20" stroke-width="1.6" fill="none"/></svg>
      </span>
      <span class="hero__or">or</span>
      <span class="hero__link">Find out what we do?</span>
    </div>
  </header>

  <h2 class="section-title ceo__title">Our CEO</h2>
  <p class="ceo__intro">Lorem ipsum dolor sit amet, consectetur adipiscing<br>elit, sed do eiusmod tempor.</p>
  <svg class="ceo__art" viewBox="0 0 556 260">
    <circle cx="437" cy="73" r="37" fill="var(--bubble)"/>
    <circle cx="540" cy="24" r="10" fill="var(--bubble)"/>
    <circle cx="145" cy="206" r="35" fill="var(--bubble)"/>
    <circle cx="67" cy="257" r="10" fill="var(--bubble)"/>
    <circle cx="242" cy="210" r="30" fill="var(--bubble)"/>
    <circle cx="320" cy="85" r="40" fill="var(--bubble)"/>
    <path d="M278 42 L372 92 Q378 96 378 104 L378 206 Q378 214 372 218 L278 266 L184 218 Q178 214 178 206 L178 104 Q178 96 184 92 Z" fill="#fff" transform="translate(0,-12)"/>
    <path d="M278 44 L368 94 L368 206 L278 254 L188 206 L188 94 Z" fill="#b89a8a" transform="translate(0,-12)" role="img" aria-label="Portrait of the CEO"/>
  </svg>

  <div class="candidates__backdrop" role="img" aria-label="Faded office team photo behind the candidates"></div>
  <h2 class="section-title candidates__title">Our Top Candidates</h2>
  <div class="grid-line grid-line--v"></div>
  <div class="grid-line grid-line--h1"></div>
  <div class="grid-line grid-line--h2"></div>

  <article class="candidate candidate--left candidate--r1"><div class="candidate__avatar" role="img" aria-label="Candidate photo"></div><h3 class="candidate__name">Mara Quill</h3><p class="candidate__role">Managing Director</p><p class="candidate__bio">Lorem ipsum dolor sit amet, consectetur adipiscing elit, sed do eiusmod tempor</p><svg class="candidate__more" width="20" height="8" viewBox="0 0 20 8"><path d="M1 4h15M13 1l4 3-4 3" stroke="#fff" stroke-width="1.6" fill="none"/></svg></article>
  <article class="candidate candidate--right candidate--r1"><div class="candidate__avatar" role="img" aria-label="Candidate photo"></div><h3 class="candidate__name">Tobin Reyes</h3><p class="candidate__role">Managing Director</p><p class="candidate__bio">Lorem ipsum dolor sit amet, consectetur adipiscing elit, sed do eiusmod tempor</p><svg class="candidate__more" width="20" height="8" viewBox="0 0 20 8"><path d="M1 4h15M13 1l4 3-4 3" stroke="#fff" stroke-width="1.6" fill="none"/></svg></article>
  <article class="candidate candidate--left candidate--r2"><div class="candidate__avatar" role="img" aria-label="Candidate photo"></div><h3 class="candidate__name">Felix Hart</h3><p class="candidate__role">Managing Director</p><p class="candidate__bio">Lorem ipsum dolor sit amet, consectetur adipiscing elit, sed do eiusmod tempor</p><svg class="candidate__more" width="20" height="8" viewBox="0 0 20 8"><path d="M1 4h15M13 1l4 3-4 3" stroke="#fff" stroke-width="1.6" fill="none"/></svg></article>
  <article class="candidate candidate--right candidate--r2"><div class="candidate__avatar" role="img" aria-label="Candidate photo"></div><h3 class="candidate__name">Owen Marsh</h3><p class="candidate__role">Managing Director</p><p class="candidate__bio">Lorem ipsum dolor sit amet, consectetur adipiscing elit, sed do eiusmod tempor</p><svg class="candidate__more" width="20" height="8" viewBox="0 0 20 8"><path d="M1 4h15M13 1l4 3-4 3" stroke="#fff" stroke-width="1.6" fill="none"/></svg></article>
  <article class="candidate candidate--left candidate--r3"><div class="candidate__avatar" role="img" aria-label="Candidate photo"></div><h3 class="candidate__name">Lena Brook</h3><p class="candidate__role">Managing Director</p><p class="candidate__bio">Lorem ipsum dolor sit amet, consectetur adipiscing elit, sed do eiusmod tempor</p><svg class="candidate__more" width="20" height="8" viewBox="0 0 20 8"><path d="M1 4h15M13 1l4 3-4 3" stroke="#fff" stroke-width="1.6" fill="none"/></svg></article>
  <article class="candidate candidate--right candidate--r3"><div class="candidate__avatar" role="img" aria-label="Candidate photo"></div><h3 class="candidate__name">Silas Crane</h3><p class="candidate__role">Managing Director</p><p class="candidate__bio">Lorem ipsum dolor sit amet, consectetur adipiscing elit, sed do eiusmod tempor</p><svg class="candidate__more" width="20" height="8" viewBox="0 0 20 8"><path d="M1 4h15M13 1l4 3-4 3" stroke="#fff" stroke-width="1.6" fill="none"/></svg></article>

  <span class="button view-all">View All
    <svg width="11" height="11" viewBox="0 0 12 12"><circle cx="6" cy="6" r="6" fill="#fff"/><path d="M5 3.5 7.5 6 5 8.5" stroke="#1b8f20" stroke-width="1.6" fill="none"/></svg>
  </span>

  <footer>
    <p class="footer__brand">VECTOR TALENT</p>
    <nav class="footer__nav"><span>About us</span><span>Candidates</span><span>Process</span><span>Feed back</span></nav>
    <p class="footer__text">Lorem ipsum dolor sit amet,<br>consectetur adipiscing elit, sed do eius</p>
    <div class="contact"><span class="contact__icon"><svg width="14" height="14" viewBox="0 0 24 24"><path d="M6.6 10.8a15 15 0 0 0 6.6 6.6l2.2-2.2a1 1 0 0 1 1-.25 11.4 11.4 0 0 0 3.6.57 1 1 0 0 1 1 1V20a1 1 0 0 1-1 1A17 17 0 0 1 3 4a1 1 0 0 1 1-1h3.5a1 1 0 0 1 1 1c0 1.25.2 2.45.57 3.57a1 1 0 0 1-.25 1z" fill="#1552a8"/></svg></span>Contact Us : 14 555 01234</div>
    <div class="social" aria-label="Social links"><span class="social__dot"></span><span class="social__dot"></span><span class="social__dot"></span><span class="social__dot"></span></div>
    <p class="footer__copy">Copyrights © 2019, The Company Name. All rights reserved.</p>
  </footer>
</section>

<!-- Variant B: full-colour hero -->
<section class="email email--photo">
  <header class="hero">
    <div class="hero__image" role="img" aria-label="Candidates seated in a row with laptops and a sketched robot, full colour"></div>
    <h1 class="hero__title">VECTOR TALENT</h1>
    <div class="hero__actions">
      <span class="button button--start">Get Started
        <svg width="11" height="11" viewBox="0 0 12 12"><circle cx="6" cy="6" r="6" fill="#fff"/><path d="M5 3.5 7.5 6 5 8.5" stroke="#1b8f20" stroke-width="1.6" fill="none"/></svg>
      </span>
      <span class="hero__or">or</span>
      <span class="hero__link">Find out what we do?</span>
    </div>
  </header>

  <h2 class="section-title ceo__title">Our CEO</h2>
  <p class="ceo__intro">Lorem ipsum dolor sit amet, consectetur adipiscing<br>elit, sed do eiusmod tempor.</p>
  <svg class="ceo__art" viewBox="0 0 556 260">
    <circle cx="437" cy="73" r="37" fill="var(--bubble)"/>
    <circle cx="540" cy="24" r="10" fill="var(--bubble)"/>
    <circle cx="145" cy="206" r="35" fill="var(--bubble)"/>
    <circle cx="67" cy="257" r="10" fill="var(--bubble)"/>
    <circle cx="242" cy="210" r="30" fill="var(--bubble)"/>
    <circle cx="320" cy="85" r="40" fill="var(--bubble)"/>
    <path d="M278 42 L372 92 Q378 96 378 104 L378 206 Q378 214 372 218 L278 266 L184 218 Q178 214 178 206 L178 104 Q178 96 184 92 Z" fill="#fff" transform="translate(0,-12)"/>
    <path d="M278 44 L368 94 L368 206 L278 254 L188 206 L188 94 Z" fill="#b89a8a" transform="translate(0,-12)" role="img" aria-label="Portrait of the CEO"/>
  </svg>

  <div class="candidates__backdrop" role="img" aria-label="Faded office team photo behind the candidates"></div>
  <h2 class="section-title candidates__title">Our Top Candidates</h2>
  <div class="grid-line grid-line--v"></div>
  <div class="grid-line grid-line--h1"></div>
  <div class="grid-line grid-line--h2"></div>

  <article class="candidate candidate--left candidate--r1"><div class="candidate__avatar" role="img" aria-label="Candidate photo"></div><h3 class="candidate__name">Mara Quill</h3><p class="candidate__role">Managing Director</p><p class="candidate__bio">Lorem ipsum dolor sit amet, consectetur adipiscing elit, sed do eiusmod tempor</p><svg class="candidate__more" width="20" height="8" viewBox="0 0 20 8"><path d="M1 4h15M13 1l4 3-4 3" stroke="#fff" stroke-width="1.6" fill="none"/></svg></article>
  <article class="candidate candidate--right candidate--r1"><div class="candidate__avatar" role="img" aria-label="Candidate photo"></div><h3 class="candidate__name">Tobin Reyes</h3><p class="candidate__role">Managing Director</p><p class="candidate__bio">Lorem ipsum dolor sit amet, consectetur adipiscing elit, sed do eiusmod tempor</p><svg class="candidate__more" width="20" height="8" viewBox="0 0 20 8"><path d="M1 4h15M13 1l4 3-4 3" stroke="#fff" stroke-width="1.6" fill="none"/></svg></article>
  <article class="candidate candidate--left candidate--r2"><div class="candidate__avatar" role="img" aria-label="Candidate photo"></div><h3 class="candidate__name">Felix Hart</h3><p class="candidate__role">Managing Director</p><p class="candidate__bio">Lorem ipsum dolor sit amet, consectetur adipiscing elit, sed do eiusmod tempor</p><svg class="candidate__more" width="20" height="8" viewBox="0 0 20 8"><path d="M1 4h15M13 1l4 3-4 3" stroke="#fff" stroke-width="1.6" fill="none"/></svg></article>
  <article class="candidate candidate--right candidate--r2"><div class="candidate__avatar" role="img" aria-label="Candidate photo"></div><h3 class="candidate__name">Owen Marsh</h3><p class="candidate__role">Managing Director</p><p class="candidate__bio">Lorem ipsum dolor sit amet, consectetur adipiscing elit, sed do eiusmod tempor</p><svg class="candidate__more" width="20" height="8" viewBox="0 0 20 8"><path d="M1 4h15M13 1l4 3-4 3" stroke="#fff" stroke-width="1.6" fill="none"/></svg></article>
  <article class="candidate candidate--left candidate--r3"><div class="candidate__avatar" role="img" aria-label="Candidate photo"></div><h3 class="candidate__name">Lena Brook</h3><p class="candidate__role">Managing Director</p><p class="candidate__bio">Lorem ipsum dolor sit amet, consectetur adipiscing elit, sed do eiusmod tempor</p><svg class="candidate__more" width="20" height="8" viewBox="0 0 20 8"><path d="M1 4h15M13 1l4 3-4 3" stroke="#fff" stroke-width="1.6" fill="none"/></svg></article>
  <article class="candidate candidate--right candidate--r3"><div class="candidate__avatar" role="img" aria-label="Candidate photo"></div><h3 class="candidate__name">Silas Crane</h3><p class="candidate__role">Managing Director</p><p class="candidate__bio">Lorem ipsum dolor sit amet, consectetur adipiscing elit, sed do eiusmod tempor</p><svg class="candidate__more" width="20" height="8" viewBox="0 0 20 8"><path d="M1 4h15M13 1l4 3-4 3" stroke="#fff" stroke-width="1.6" fill="none"/></svg></article>

  <span class="button view-all">View All
    <svg width="11" height="11" viewBox="0 0 12 12"><circle cx="6" cy="6" r="6" fill="#fff"/><path d="M5 3.5 7.5 6 5 8.5" stroke="#1b8f20" stroke-width="1.6" fill="none"/></svg>
  </span>

  <footer>
    <p class="footer__brand">VECTOR TALENT</p>
    <nav class="footer__nav"><span>About us</span><span>Candidates</span><span>Process</span><span>Feed back</span></nav>
    <p class="footer__text">Lorem ipsum dolor sit amet,<br>consectetur adipiscing elit, sed do eius</p>
    <div class="contact"><span class="contact__icon"><svg width="14" height="14" viewBox="0 0 24 24"><path d="M6.6 10.8a15 15 0 0 0 6.6 6.6l2.2-2.2a1 1 0 0 1 1-.25 11.4 11.4 0 0 0 3.6.57 1 1 0 0 1 1 1V20a1 1 0 0 1-1 1A17 17 0 0 1 3 4a1 1 0 0 1 1-1h3.5a1 1 0 0 1 1 1c0 1.25.2 2.45.57 3.57a1 1 0 0 1-.25 1z" fill="#1552a8"/></svg></span>Contact Us : 14 555 01234</div>
    <div class="social" aria-label="Social links"><span class="social__dot"></span><span class="social__dot"></span><span class="social__dot"></span><span class="social__dot"></span></div>
    <p class="footer__copy">Copyrights © 2019, The Company Name. All rights reserved.</p>
  </footer>
</section>

</body>
</html>
```